"Vantarel Inc." Needs a Logo Design and Business Card

The name of the company is "Vantarel Inc."
Our Business decription, which should appear on the front of the Business Card along with the logo and business name is:
"Boutique Global Procurement and Management Services"
We offer the following SERVICES that should be listed on the back of the Business Card :
"Consultants"
"Management"
"Business Research & Development"
"Sourcing Agent"
"Distributors"
We would like to see designs that use the colors
burnt orange and,
stainless steel
Business card designs should be innovatively modern and contemporary
Telephone number and email address should be on the back of the card
Updates
The name of the firm is "Vantarel Inc.
Industry/Entity Type
Steel
Look and feel
Each slider illustrates characteristics of the customer's brand and the style your logo design should communicate.

```html
<!DOCTYPE html>
<html lang="en">
<head>
<meta charset="utf-8">
<title>Vantarel Inc. — Business Card</title>
<link rel="stylesheet" href="https://fonts.googleapis.com/css2?family=Arimo:wght@400&display=swap">
<style>
  :root {
    --burnt-orange: #ea6f00;
    --steel: #505050;
    --steel-text: #4e4e4e;
    --card-white: #ffffff;
    --edge: #5a5a5a;
  }
  * { margin: 0; padding: 0; box-sizing: border-box; }
  html, body {
    width: 1200px;
    height: 344px;
    overflow: hidden;
    background: var(--card-white);
  }
  .card-spread {
    position: relative;
    width: 1200px;
    height: 344px;
    border: 1px solid var(--edge);
    font-family: "Arimo", Arial, Helvetica, sans-serif;
    overflow: hidden;
  }
  .card-front {
    position: absolute;
    left: 0; top: 0;
    width: 601px;
    height: 100%;
    background: var(--burnt-orange);
  }
  .brand-mark {
    position: absolute;
    left: 96px; top: 50px;
    width: 405px; height: 193px;
    background: var(--steel);
    display: flex;
    align-items: center;
    justify-content: center;
  }
  .brand-name {
    color: #2f2f2f;
    font-size: 22px;
    font-weight: 400;
  }
  .tagline {
    position: absolute;
    left: 0; width: 601px;
    top: 287px;
    text-align: center;
    color: var(--steel-text);
    font-size: 21px;
  }
  .card-back {
    position: absolute;
    left: 601px; top: 0;
    width: 599px; height: 100%;
    background: var(--card-white);
  }
  .frame-lines {
    position: absolute;
    left: 0; top: 0;
  }
  .phone {
    position: absolute;
    left: 36px; top: 36px;
    color: var(--burnt-orange);
    font-size: 20px;
  }
  .services {
    position: absolute;
    right: 40px; top: 86px;
    list-style: none;
    text-align: right;
    color: var(--steel-text);
    font-size: 21px;
    line-height: 29px;
  }
  .address {
    position: absolute;
    left: 40px; top: 283px;
    color: var(--burnt-orange);
    font-size: 20px;
  }
</style>
</head>
<body>
  <div class="card-spread">
    <section class="card-front">
      <div class="brand-mark">
        <span class="brand-name">Vantarel Inc.</span>
      </div>
      <p class="tagline">Boutique Global Procurement and Service Solutions</p>
    </section>
    <section class="card-back">
      <svg class="frame-lines" width="599" height="344" viewBox="0 0 599 344" aria-hidden="true">
        <rect x="27" y="20" width="546" height="306" fill="none" stroke="var(--burnt-orange)" stroke-width="2"/>
        <rect x="33" y="26" width="534" height="294" fill="none" stroke="var(--burnt-orange)" stroke-width="2"/>
      </svg>
      <p class="phone">123.123.1234</p>
      <ul class="services">
        <li>Distributor</li>
        <li>Consultant</li>
        <li>Management</li>
        <li>Sourcing Agent</li>
        <li>Business Research</li>
        <li>&amp; Development</li>
      </ul>
      <p class="address">Adress goes here. . . . .</p>
    </section>
  </div>
</body>
</html>
```